Podiatry clinic requires a modern revamp and editing of existing website.

I would like a fresh new look and updated information for my current business website. An easy to navigate site with prominent address and phone number for call to action. We are a podiatry clinic that focuses on general and sports podiatry.
I would like 4 pages; including Home page, About Us, Services & Contact.
www.harbourlanefootcare.com

Target Market(s)

Active working professionals.

Industry/Entity Type

Medical

Coding

Coded - Design and coding required

Number of Pages Required

4 page

Font styles to use
Sans Serif

Colors
6b449b

Requirements
Must have
• A modern look with logo and active images; clean and uncluttered. Visible phone number and address for call to action.
• 4 pages - Home, About Us, Services, Contact.
• Home page - update address & service logos.
• About Us - update of personal information.
• Services - Revamp of existing page.
• Contact page to include Google map, email & phone number.
Nice to have
• Ability to add content easily; eg. a blog or adding video onto Home page.
• Link to Facebook page.

```html
<!DOCTYPE html>
<html lang="en">
<head>
<meta charset="utf-8">
<title>Harbour Lane Foot Care — Home</title>
<link href="https://fonts.googleapis.com/css2?family=Raleway:wght@400;500;600&family=Arimo:wght@400;700&family=PT+Sans:wght@700&display=swap" rel="stylesheet">
<style>
:root{
  --purple:#6b449b;
  --purple-light:#9b85c4;
  --purple-deep:#4a2f8f;
  --yellow:#f7c600;
  --orange:#ff6a1a;
  --grey:#666666;
  --grey-dark:#4f4f4f;
  --ink:#222222;
  --white:#ffffff;
}
*{margin:0;padding:0;box-sizing:border-box}
html,body{width:816px;height:1200px;overflow:hidden}
body{position:relative;font-family:"Arimo",Arial,sans-serif;color:var(--ink);background:var(--white)}
.abs{position:absolute}

/* header */
.site-header{left:0;top:0;width:816px;height:61px;background:var(--purple-light);border-top:2px solid var(--purple-deep)}
.nav-marker{left:330px;top:0;width:30px;height:3px;background:var(--orange)}
.brand{left:96px;top:10px;display:flex;align-items:center;gap:6px}
.brand-dot{width:14px;height:14px;border-radius:50%;background:var(--purple-deep)}
.brand-name{font-family:"Raleway",sans-serif;font-weight:600;font-size:11px;line-height:13px;color:var(--white);width:70px}
.main-nav{left:330px;top:36px;display:flex;gap:22px;font-family:"Raleway",sans-serif;font-weight:500;font-size:12px;color:var(--white)}
.main-nav .active{color:var(--orange)}
.nav-divider{left:597px;top:14px;width:1px;height:38px;background:rgba(255,255,255,.6)}
.call{left:615px;top:24px;display:flex;gap:8px;align-items:center;color:var(--white)}
.call-label{font-family:"Raleway",sans-serif;font-size:10px;line-height:12px}
.call-number{font-family:"Arimo",sans-serif;font-size:14px;color:#2e2e2e}

/* hero */
.hero{left:0;top:61px;width:816px;height:245px;display:flex}
.hero-panel{height:100%}
.hero-arrow{top:141px;width:22px;height:24px;border:1px solid rgba(255,255,255,.7);background:rgba(0,0,0,.25)}
.tagline{left:0;top:306px;width:816px;height:35px;background:var(--purple);color:var(--white);font-family:"Raleway",sans-serif;font-size:16px;font-weight:500;text-align:center;line-height:35px}
.tagline b{font-weight:600}

/* service cards */
.service-card{top:357px;height:198px;overflow:hidden}
.service-title{height:28px;background:var(--yellow);font-family:"PT Sans",sans-serif;font-weight:700;font-size:13px;color:var(--purple);text-align:center;line-height:30px}
.service-photo{height:170px}
.service-caption{position:absolute;left:0;bottom:0;width:100%;height:58px;background:rgba(107,68,155,.82);color:var(--white);font-size:9px;line-height:16.5px;text-align:center;padding:4px 10px}

/* welcome */
.welcome-shade{left:0;top:578px;width:816px;height:30px;background:linear-gradient(#ececec,#fff)}
.welcome-accent{left:0;top:578px}
.section-title{width:816px;left:0;text-align:center;font-family:"Raleway",sans-serif;font-weight:500}
.welcome-title{top:604px;font-size:18px;color:#2a2a4a}
.rule{left:214px;width:370px;height:6px}
.welcome-copy{left:100px;top:655px;width:616px;text-align:center;font-size:10.2px;line-height:18.4px;color:#333}
.welcome-cta{left:100px;top:736px;width:616px;text-align:center;font-size:10.2px;line-height:17px;font-weight:700;color:#222}

/* accreditations */
.accreditations{left:0;top:790px;width:816px;height:209px;background:var(--grey);overflow:hidden}
.accred-title{top:804px;font-size:22px;color:var(--white);font-family:"Arimo",sans-serif;font-weight:400}
.badge{top:880px;width:139px;height:53px;background:var(--white);display:flex;align-items:center;justify-content:center}
.badge span{display:block;width:90px;height:22px;border-radius:3px}

/* footer */
.site-footer{left:0;top:999px;width:816px;height:171px;background:var(--purple-light);color:#2b2b2b}
.footer-heading{top:1016px;font-family:"Raleway",sans-serif;font-size:12.5px;font-weight:500;color:#3c3c3c;padding-bottom:6px;border-bottom:1px solid rgba(255,255,255,.35)}
.quick-links{left:92px;top:1047px;list-style:none;font-family:"Raleway",sans-serif;font-size:9.5px;line-height:17px}
.quick-links li::before{content:"›";color:var(--white);margin-right:6px}
.col-rule{top:1040px;width:1px;height:108px;background:rgba(255,255,255,.3)}
.contact-item{left:245px;font-family:"Raleway",sans-serif;font-size:9.5px;line-height:11.5px;display:flex;gap:8px;width:165px;padding-bottom:10px;border-bottom:1px solid rgba(255,255,255,.3)}
.hours-item{left:473px;font-family:"Raleway",sans-serif;font-size:9.5px;line-height:12.5px;width:115px;padding-bottom:7px;border-bottom:1px solid rgba(255,255,255,.3)}
.footer-brand{left:620px;top:1050px;display:flex;gap:6px;align-items:flex-start}
.footer-brand .brand-dot{width:18px;height:18px;margin-top:2px}
.footer-brand .brand-name{font-size:15px;line-height:20px;width:95px}
.bottom-bar{left:0;top:1170px;width:816px;height:30px;background:var(--grey-dark)}
.copyright{left:90px;top:1178px;font-family:"Raleway",sans-serif;font-size:9.5px;color:#e6e6e6}
.social{top:1172px;width:23px;height:23px;border-radius:50%;background:#6e6e6e}
</style>
</head>
<body>

<header class="abs site-header"></header>
<div class="abs nav-marker"></div>
<div class="abs brand"><span class="brand-dot"></span><span class="brand-name">Harbour Lane Foot Care</span></div>
<nav class="abs main-nav"><span class="active">Home</span><span>About Us</span><span>Services</span><span>Contact Us</span></nav>
<div class="abs nav-divider"></div>
<div class="abs call">
  <svg width="22" height="22" viewBox="0 0 22 22"><circle cx="11" cy="11" r="10" fill="none" stroke="#fff" stroke-width="1.3"/><path d="M8 6c-1 1-1 3 1 6s4 4 5 4l1.5-1.5-2-2-1 .7c-1-.6-2-1.8-2.5-3l.8-1-1.7-2.2z" fill="#fff"/></svg>
  <div><div class="call-label">Call Us Today</div><div class="call-number">1300 555 208</div></div>
</div>

<section class="abs hero">
  <div class="hero-panel" style="width:95px;background:linear-gradient(#5b8c5e,#3c6b3f)" role="img" aria-label="Golfer in green shirt putting on a course"></div>
  <div class="hero-panel" style="width:163px;background:linear-gradient(#8aa070,#6f7d64)" role="img" aria-label="Woman running a race on a grassy path"></div>
  <div class="hero-panel" style="width:152px;background:linear-gradient(#6e8fc0,#7c7a5c)" role="img" aria-label="Cyclists racing on a road"></div>
  <div class="hero-panel" style="width:188px;background:linear-gradient(#3a3a3a,#9a9a9a)" role="img" aria-label="Dancer leaping in black and white"></div>
  <div class="hero-panel" style="width:138px;background:linear-gradient(#b4683a,#8b3d20)" role="img" aria-label="Footballer kicking a ball on a dirt field"></div>
  <div class="hero-panel" style="width:80px;background:linear-gradient(#6a5a4c,#3a2f2a)" role="img" aria-label="Basketball player shooting in an arena"></div>
</section>
<div class="abs hero-arrow" style="left:8px"><svg width="20" height="22"><path d="M12 7l-4 4 4 4" stroke="#fff" fill="none" stroke-width="1.6"/></svg></div>
<div class="abs hero-arrow" style="left:786px"><svg width="20" height="22"><path d="M8 7l4 4-4 4" stroke="#fff" fill="none" stroke-width="1.6"/></svg></div>
<div class="abs tagline"><b>harbour lane foot care</b> is a podiatry clinic in the heart of melbourne CBD</div>

<article class="abs service-card" style="left:86px;width:197px">
  <div class="service-title">Sports Injuries</div>
  <div class="service-photo" style="background:linear-gradient(#9aa3a8,#6f6f6f)" role="img" aria-label="Runner holding an injured ankle on a road"></div>
  <p class="service-caption">Lorem ipsum dolor sit amet, consectetuer adipiscing elit, sed diam nonummy nibh euismod tincidunt ut laoreet.</p>
</article>
<article class="abs service-card" style="left:307px;width:194px">
  <div class="service-title">Orthotic Therapy</div>
  <div class="service-photo" style="background:linear-gradient(#ebe4dc,#cdb39c)" role="img" aria-label="Podiatrist fitting an orthotic insole to a foot"></div>
  <p class="service-caption">Lorem ipsum dolor sit amet, consectetuer adipiscing elit, sed diam nonummy nibh euismod tincidunt ut laoreet.</p>
</article>
<article class="abs service-card" style="left:530px;width:195px">
  <div class="service-title">Nail Surgery</div>
  <div class="service-photo" style="background:linear-gradient(#c9c6c8,#d9a088)" role="img" aria-label="Gloved hands giving an injection to a toe"></div>
  <p class="service-caption">Lorem ipsum dolor sit amet, consectetuer adipiscing elit, sed diam nonummy nibh euismod tincidunt ut laoreet.</p>
</article>

<div class="abs welcome-shade"></div>
<svg class="abs welcome-accent" width="200" height="145"><polygon points="0,0 196,0 0,143" fill="#f7c600"/></svg>
<h1 class="abs section-title welcome-title">Welcome to Harbour Lane Foot Care</h1>
<svg class="abs rule" style="top:633px" width="370" height="6"><rect x="0" y="0" width="6" height="5" fill="#f7c600"/><rect x="13" y="0" width="6" height="5" fill="#4a2f8f"/><rect x="26" y="1.5" width="318" height="2" fill="#f7c600"/><rect x="350" y="0" width="6" height="5" fill="#4a2f8f"/><rect x="363" y="0" width="6" height="5" fill="#f7c600"/></svg>
<p class="abs welcome-copy">Harbour Lane Foot Care is a Podiatry clinic in the heart of Melbourne CBD. We are located between Elder &amp; Marsh Streets in the Pacific Trade Centre / Linden Hotel Complex. Our podiatrists are fully qualified health professionals who are able to diagnose, treat, manage or help to prevent all medical conditions that affect the feet and lower limb.We provide General Podiatry Treatment and some Specialised Services in relation to various foot conditions, including Sports Injuries, Orthotic Therapy and Nail Surgery.</p>
<p class="abs welcome-cta">For Appointments or Enquiries please<br>call us on 1300 555 208 &nbsp;or email: &nbsp;info@harbourlanefootcare.com</p>

<section class="abs accreditations">
  <svg class="abs" style="left:0;top:0" width="816" height="209"><polygon points="816,76 816,209 635,209" fill="#4a2f8f"/></svg>
</section>
<h2 class="abs section-title accred-title">Our Accreditations</h2>
<svg class="abs rule" style="top:842px" width="370" height="6"><rect x="0" y="0" width="6" height="5" fill="#f7c600"/><rect x="13" y="0" width="6" height="5" fill="#4a2f8f"/><rect x="26" y="1.5" width="318" height="2" fill="#f7c600"/><rect x="350" y="0" width="6" height="5" fill="#4a2f8f"/><rect x="363" y="0" width="6" height="5" fill="#f7c600"/></svg>
<div class="abs badge" style="left:119px"><span style="background:#3a5aa8"></span></div>
<div class="abs badge" style="left:272px"><span style="background:#1d5fa8"></span></div>
<div class="abs badge" style="left:426px"><span style="background:#2b2b2b"></span></div>
<div class="abs badge" style="left:579px"><span style="background:#119a4a"></span></div>

<footer class="abs site-footer"></footer>
<h3 class="abs footer-heading" style="left:92px;width:90px">Quick Links</h3>
<ul class="abs quick-links"><li>Consulting</li><li>Inspections</li><li>Training</li><li>General Contracing</li><li>Clients</li><li>Contact Us</li></ul>
<div class="abs col-rule" style="left:214px"></div>
<h3 class="abs footer-heading" style="left:243px;width:167px">Contact Details</h3>
<div class="abs contact-item" style="top:1047px"><svg width="8" height="11" viewBox="0 0 8 11"><path d="M4 0a4 4 0 0 1 4 4c0 3-4 7-4 7S0 7 0 4a4 4 0 0 1 4-4z" fill="#2b2b2b"/><circle cx="4" cy="4" r="1.4" fill="#9b85c4"/></svg><span>Suite 214 / 36 Lantern<br>Street &nbsp;Melbourne &nbsp;3000</span></div>
<div class="abs contact-item" style="top:1092px"><svg width="10" height="10" viewBox="0 0 10 10"><path d="M2 0l2 2.5-1 1.2c.6 1.3 1.7 2.4 3 3l1.2-1L10 8l-1.6 1.7C6 10 0 4 .3 1.6z" fill="#2b2b2b"/></svg><span>1300 555 208</span></div>
<div class="abs contact-item" style="top:1128px;border:none"><svg width="10" height="8" viewBox="0 0 10 8"><rect width="10" height="8" fill="#2b2b2b"/><path d="M0 0l5 4 5-4" stroke="#9b85c4" fill="none"/></svg><span>info@harbourlanefootcare.com</span></div>
<div class="abs col-rule" style="left:443px"></div>
<h3 class="abs footer-heading" style="left:472px;width:115px">Hours of Operation</h3>
<p class="abs hours-item" style="top:1047px">Monday to Friday<br>10:00am to 07:00pm</p>
<p class="abs hours-item" style="top:1085px">Saturday<br>10:00am to 05:00pm</p>
<p class="abs hours-item" style="top:1123px;border:none">Sunday<br>By Appointment Only</p>
<div class="abs footer-brand"><span class="brand-dot"></span><span class="brand-name">Harbour Lane Foot Care</span></div>

<div class="abs bottom-bar"></div>
<p class="abs copyright">Copyright © 2016 Harbour Lane Foot Care. &nbsp;All Right Reserved.</p>
<div class="abs social" style="left:631px"></div>
<div class="abs social" style="left:660px"></div>
<div class="abs social" style="left:689px"></div>

</body>
</html>
```